Harbor LunaVital & Equipments

I need to create full stationery design for the company; Business Card, Envelop, Letterheads, Calendar and email template.

Our company is specialized in the import and export of nutritional, pharmaceutical and cosmetics in addition to medical equipments.

These is no limitation on how to use colors within the design.

Target Market(s)

Global

Industry/Entity Type

Healthcare

Other font styles liked:
• a font close to logo. Letterhead body text to be different than the address text

Requirements
Nice to have
• We will have multiple locations so it is good to keep space for future addresses.
• Stationary requirements:
• Letterhead: A4
• Envelopes: 3 regular sizes : large, medium and small (i do not know the sizes)
• Colors: extracted from the logo

```html
<!DOCTYPE html>
<html lang="en">
<head>
<meta charset="utf-8">
<title>Harbor LunaVital &amp; Equipments – Envelopes</title>
<link href="https://fonts.googleapis.com/css2?family=Ubuntu:wght@400;500;700&display=swap" rel="stylesheet">
<style>
  :root {
    --backdrop: #262626;
    --paper: #ffffff;
    --navy: #0b0b5c;
    --orange: #f9a928;
    --green: #1f9a22;
    --sky: #29a8e0;
    --ink: #2b2b2b;
    --tint: #e6e7f0;
  }
  * { margin: 0; padding: 0; box-sizing: border-box; }
  html, body { width: 1200px; height: 1200px; overflow: hidden; background: var(--backdrop); }
  body { position: relative; font-family: "Ubuntu", sans-serif; }

  .envelope {
    position: absolute;
    background: var(--paper);
    overflow: hidden;
  }
  .envelope--small { left: 264px; top: 186px; width: 606px; height: 302px; }
  .envelope--large { left: 264px; top: 631px; width: 604px; height: 425px; }

  .brand {
    position: absolute;
    display: flex;
    align-items: center;
    gap: 8px;
    color: var(--sky);
    font-weight: 700;
    line-height: 1.05;
  }
  .brand__mark { background: var(--navy); flex: none; border-radius: 3px; }
  .envelope--small .brand { left: 40px; top: 26px; font-size: 17px; }
  .envelope--small .brand__mark { width: 22px; height: 22px; }
  .envelope--large .brand { left: 50px; top: 40px; font-size: 22px; }
  .envelope--large .brand__mark { width: 28px; height: 28px; }

  .watermark {
    position: absolute;
    right: 0;
    bottom: 8px;
    background: linear-gradient(135deg, rgba(230,231,240,0) 0%, var(--tint) 100%);
  }
  .envelope--small .watermark { width: 300px; height: 294px; }
  .envelope--large .watermark { width: 280px; height: 300px; }

  .address {
    position: absolute;
    color: var(--ink);
    font-weight: 400;
    letter-spacing: 0.04em;
  }
  .envelope--small .address { left: 40px; top: 258px; font-size: 7.5px; line-height: 11px; }
  .envelope--large .address { left: 50px; top: 355px; font-size: 10.5px; line-height: 15px; }
  .address__web { font-weight: 500; }

  .colour-band {
    position: absolute;
    left: 0; right: 0; bottom: 0;
    height: 8px;
    display: flex;
  }
  .colour-band span { display: block; height: 100%; }
  .colour-band .navy { background: var(--navy); flex: 24; }
  .colour-band .orange { background: var(--orange); flex: 25.5; }
  .colour-band .green { background: var(--green); flex: 25.5; }
  .colour-band .sky { background: var(--sky); flex: 25; }
</style>
</head>
<body>

  <section class="envelope envelope--small">
    <div class="watermark" role="img" aria-label="Faint large brand decoration"></div>
    <div class="brand">
      <span class="brand__mark"></span>
      <span class="brand__name">Harbor LunaVital<br>&amp; Equipments</span>
    </div>
    <p class="address">
      1870 Meridian Avenue, Oakland, California 94610<br>
      <span class="address__web">www.harborlunavital.com</span>
    </p>
    <div class="colour-band"><span class="navy"></span><span class="orange"></span><span class="green"></span><span class="sky"></span></div>
  </section>

  <section class="envelope envelope--large">
    <div class="watermark" role="img" aria-label="Faint large brand decoration"></div>
    <div class="brand">
      <span class="brand__mark"></span>
      <span class="brand__name">Harbor LunaVital<br>&amp; Equipments</span>
    </div>
    <p class="address">
      1870 Meridian Avenue, Oakland,<br>
      California 94610<br>
      <span class="address__web">www.harborlunavital.com</span>
    </p>
    <div class="colour-band"><span class="navy"></span><span class="orange"></span><span class="green"></span><span class="sky"></span></div>
  </section>

</body>
</html>
```